Family History Site Home Page Redesign

KinTrailo (http://www.kintrailo.example) is a new genealogy website. We would like a fresh home page. We provide innovative tools for the serious genealogist in a Chatterbay-like environment. The tagline is “Easy to research. Easy to share.” The page must convey both the research and sharing aspects of the product and benefits such as:
• Modern
• Intuitive
• Easy
• Free
• Fast (Save 90% data entry time)
• Integrate with LineageVault
• Control your tree; nobody can edit without your permission
Our target audience is women age 30-60. Please examine our current home page at KinTrailo.example. You will be creating a revised homepage that appeals to this demographic. Feel free to use any part of the existing page. You may use any of the materials provided, but you are not required to use everything.
You may use other images as long as you have the copyright or it is public domain. For instance, you could show an image of a woman, teenager, or young adult enjoying an ziphandset or tablet, a civil war soldier, a wagon train, etc.
Please stay with the Layered Canvas style (Use Roboto font and other guidelines from https://layeredcanvas.example/guidelines/layered-canvas/introduction.html) and our color palette (brand guidelines included).
We would like the following elements:
• Header (must keep login link in upper right corner)
• Primary call to action (Currently “Get started”)
• Section about “Easy to Research” with link to read more
• Section about “Easy to Share” with link to read more
• Section about LineageVault integration with link to read more
Optional:
• Marisol's Story (video)
• Links to demo trees and pages for Gerald Pemberly and/or Warren Ashcombe
• Pricing section – please include and do not change
• Footer with the same links it now has.

The homepage must be responsive so it can be viewed on mobile phones and tablets.

Here are some examples of homepages we like:
https://www.brightquorn.example/vexa/
https://www.heritagloom.example/dna/
https://www.probepanel.example/
https://snapfolio.example/
https://www.zoomcab.example/
http://www.lineagevault.example

Target Market(s)

women 30-60

Number of Pages Required

1 page

Font styles to use
Sans Serif

Requirements
Must have
• Sections for "Easy to Research," "Easy to Share," and "LineageVault Integration," with "learn more" links.
• Pricing section.
• Our basic plan is free forever.
Nice to have
• Happy family or happy person with a computer. Most of the homepages we have liked concentrated on people's faces. Please find public domain pictures or have copyright to pictures.
• What is KinTrailo section.
• Section for 1-3 sample videos. KinTrailo makes slideshow videos from family photos.Please make sure it is obvious that these are sample videos.
• Place for Marisol's video and/or the walk through.

```html
<!DOCTYPE html>
<html lang="en">
<head>
<meta charset="utf-8">
<title>KinTrailo – Easy to Research, Easy to Share</title>
<link rel="stylesheet" href="https://fonts.googleapis.com/css2?family=Roboto:wght@300;400;500&family=Open+Sans:wght@400;600&display=swap">
<style>
:root{
  --green:#6cc42f;
  --green-soft:#c6e8ae;
  --blue:#5b9bd3;
  --slate:#4e6479;
  --yellow:#fdd12b;
  --gold:#f6c02a;
  --gold-soft:#fcebb0;
  --navy:#2c4c69;
  --ink:#2d4e6b;
  --text:#222;
  --muted:#8a8a8a;
  --line:#d6d6d6;
  --band:#f1f1f1;
  --white:#fff;
}
*{box-sizing:border-box;margin:0;padding:0}
html,body{width:1200px;height:2748px;overflow:hidden;background:var(--white)}
body{position:relative;font-family:"Roboto",Arial,sans-serif;color:var(--text)}
.abs{position:absolute}

/* hero */
.hero{left:0;top:0;width:1200px;height:660px;overflow:hidden}
.hero-photo{position:absolute;inset:0;background:
  radial-gradient(ellipse at 30% 45%,#d9b89a 0%,#c9a98c 18%,transparent 40%),
  radial-gradient(ellipse at 22% 85%,#9fb8cf 0%,transparent 35%),
  linear-gradient(100deg,#b9b3aa 0%,#dcd8d2 45%,#eceae6 70%,#e4e2df 100%)}
.brand{left:119px;top:30px;font:500 44px/1 "Roboto",Arial,sans-serif;color:var(--green);letter-spacing:-.5px;display:flex;align-items:center;gap:10px}
.brand-dot{width:14px;height:14px;border-radius:50%;background:var(--green)}
.btn-head{top:33px;width:113px;height:40px;font:400 18px/36px "Roboto",Arial,sans-serif;text-align:center;text-decoration:none}
.btn-signup{left:854px;border:2px solid var(--slate);color:var(--slate);background:var(--white)}
.btn-login{left:980px;background:var(--blue);color:var(--white);line-height:40px}
.hero-disc{left:680px;top:160px;width:384px;height:384px;border-radius:50%;background:rgba(108,196,47,.95);color:var(--white);text-align:center;padding-top:110px}
.hero-disc h1{font:300 36px/44px "Roboto",Arial,sans-serif}
.hero-disc p{font:400 14px/22px "Open Sans",Arial,sans-serif;margin:10px auto 0;width:270px}
.btn-start{display:inline-block;margin-top:20px;border:2px solid var(--white);color:var(--white);font:400 17px/40px "Roboto",Arial,sans-serif;width:178px;height:44px;text-decoration:none;letter-spacing:.5px}

/* features */
.feature{top:690px;width:300px;text-align:center}
.feature-icon{width:146px;height:146px;border-radius:50%;margin:0 auto;display:flex;align-items:center;justify-content:center}
.feature h2{font:400 22px/1 "Roboto",Arial,sans-serif;margin-top:24px}
.feature p{font:400 12.5px/21px "Open Sans",Arial,sans-serif;color:var(--muted);margin:14px auto 0;width:290px}
.btn-more{display:inline-block;margin-top:18px;width:139px;height:37px;font:500 14px/33px "Roboto",Arial,sans-serif;border:2px solid;text-decoration:none;letter-spacing:.5px}
.f-research{left:128px}.f-research .feature-icon{background:var(--slate)}.f-research h2{color:var(--text)}.f-research .btn-more{color:var(--slate);border-color:var(--slate)}
.f-share{left:451px}.f-share .feature-icon{background:var(--blue)}.f-share h2{color:var(--blue)}.f-share .btn-more{color:var(--blue);border-color:var(--blue)}
.f-sync{left:775px}.f-sync .feature-icon{background:var(--yellow)}.f-sync h2{color:var(--yellow)}.f-sync .btn-more{color:var(--yellow);border-color:var(--yellow)}

/* story */
.story{left:0;top:1130px;width:1200px;height:561px;background:var(--band);overflow:hidden}
.section-title{left:0;width:1200px;text-align:center;font:400 26px/1 "Roboto",Arial,sans-serif;color:var(--ink);letter-spacing:.5px}
.section-title span{color:var(--blue)}
.leaf{left:584px}
.video{left:311px;top:1240px;width:579px;height:336px;background:
  radial-gradient(ellipse at 55% 50%,#e9ecef 0%,#c9ced3 22%,transparent 40%),
  linear-gradient(160deg,#3a3735 0%,#5a554f 40%,#2a2826 100%)}
.play{left:551px;top:1358px}
.btn-story{top:1607px;height:38px;font:500 14px/34px "Roboto",Arial,sans-serif;text-align:center;text-decoration:none;letter-spacing:.3px}
.btn-demo{left:390px;width:205px;background:var(--green);color:var(--white);line-height:38px}
.btn-pages{left:603px;width:205px;border:2px solid #9aa0a6;color:#333;background:#f4f4f4}

/* pricing */
.plan{top:1825px;width:326px;height:423px;border:2px solid var(--line);padding:30px 0 0 18px}
.plan-name{font:500 19px/1 "Roboto",Arial,sans-serif;text-align:center;margin-left:-18px;letter-spacing:.3px}
.plan-price{font:400 18px/1 "Roboto",Arial,sans-serif;text-align:center;margin:12px 0 0 -18px}
.plan ul{list-style:none;margin-top:32px}
.plan li{display:flex;align-items:center;gap:8px;height:32px;font:400 13px/1 "Open Sans",Arial,sans-serif;color:#555}
.tick{flex:none;width:18px;height:18px}
.p-free{left:97px}.p-free .plan-name,.p-free .plan-price,.p-free .tick{color:var(--green)}
.p-free .tick.faded{color:var(--green-soft)}
.p-std{left:436px}.p-std .plan-name,.p-std .plan-price,.p-std .tick{color:var(--gold)}
.p-std .tick.faded{color:var(--gold-soft)}
.p-pro{left:777px}.p-pro .plan-name,.p-pro .plan-price,.p-pro .tick{color:var(--blue)}
.footnote{left:0;top:2300px;width:1200px;text-align:center;font:400 12px/1 "Open Sans",Arial,sans-serif;color:#999}

/* footer */
.footer{left:0;top:2372px;width:1200px;height:376px;background:var(--navy)}
.fcol{top:2432px;color:var(--white)}
.fcol h3{font:400 22px/1 "Roboto",Arial,sans-serif}
.fcol ul{list-style:none;margin-top:18px}
.fcol li{font:400 15px/31px "Roboto",Arial,sans-serif}
.fcol a{color:var(--white);text-decoration:none}
.social{display:flex;gap:6px;margin-top:18px}
.social span{width:32px;height:32px;border:2px solid var(--white);border-radius:50%}
.fbadge{left:838px;top:2420px;width:200px;height:200px;border-radius:50%;background:var(--white);border:14px solid var(--blue);box-shadow:inset 0 0 0 10px var(--green)}
.frule{left:110px;top:2678px;width:980px;height:1px;background:rgba(255,255,255,.2)}
.copyright{left:0;top:2702px;width:1200px;text-align:center;font:400 13px/1 "Open Sans",Arial,sans-serif;color:rgba(255,255,255,.6)}
</style>
</head>
<body>
<svg width="0" height="0" style="position:absolute">
  <symbol id="tick" viewBox="0 0 18 18"><circle cx="9" cy="9" r="9" fill="currentColor"/><path d="M5 9.3l2.7 2.7L13 6.5" fill="none" stroke="#fff" stroke-width="2"/></symbol>
  <symbol id="sprout" viewBox="0 0 32 20"><path d="M16 20C14 10 8 4 0 4c2 8 8 12 16 12zM16 20C18 10 24 2 32 2c-2 8-8 12-16 14z" fill="#6cc42f"/></symbol>
</svg>

<header>
  <div class="abs hero" role="img" aria-label="Photo of a smiling mother and her son looking at a tablet on a sofa"><div class="hero-photo"></div></div>
  <div class="abs brand"><span class="brand-dot"></span>KinTrailo</div>
  <a class="abs btn-head btn-signup" href="#">Sign Up</a>
  <a class="abs btn-head btn-login" href="#">Log In</a>
  <div class="abs hero-disc">
    <h1>Easy to Research<br>Easy to Share</h1>
    <p>Praesent elementum elit at tellus nec ultricies sit amet porttitor mattis enim in</p>
    <a class="btn-start" href="#">GET STARTED</a>
  </div>
</header>

<section class="features">
  <div class="abs feature f-research">
    <div class="feature-icon"><svg width="64" height="84" viewBox="0 0 64 84"><rect x="4" y="2" width="56" height="80" rx="6" fill="none" stroke="#fff" stroke-width="3"/><rect x="11" y="10" width="42" height="58" fill="none" stroke="#fff" stroke-width="2"/><circle cx="32" cy="75" r="3" fill="#fff"/></svg></div>
    <h2>Easy to Research</h2>
    <p>Get hints from LineageVault, Ancestrel, and other partners...you don't even need to sync your tree with LineageVault to get hints.</p>
    <a class="btn-more" href="#">READ MORE</a>
  </div>
  <div class="abs feature f-share">
    <div class="feature-icon"><svg width="76" height="66" viewBox="0 0 76 66" fill="none" stroke="#fff" stroke-width="4" stroke-linejoin="round"><path d="M8 32V20h54M52 8l12 12-12 12"/><path d="M68 34v12H14M24 58L12 46l12-12"/></svg></div>
    <h2>Easy to Share</h2>
    <p>Pinboardly-like Media Wall lets family members browse around to find what they like. No subscription required</p>
    <a class="btn-more" href="#">READ MORE</a>
  </div>
  <div class="abs feature f-sync">
    <div class="feature-icon"><svg width="84" height="64" viewBox="0 0 84 64" fill="none" stroke="#fff" stroke-width="3"><rect x="2" y="2" width="80" height="60"/><rect x="12" y="12" width="60" height="40"/><path d="M2 2l10 10M82 2L72 12M2 62l10-10M82 62L72 52"/><circle cx="32" cy="28" r="5"/><circle cx="52" cy="28" r="5"/><path d="M22 48c0-8 5-12 10-12s10 4 10 12M42 48c0-8 5-12 10-12s10 4 10 12"/></svg></div>
    <h2>LineageVault Integration</h2>
    <p>Sync your tree, documents, and memories with LineageVault but you control your tree. No one can change it without your permission</p>
    <a class="btn-more" href="#">READ MORE</a>
  </div>
</section>

<section>
  <div class="abs story"><svg width="1200" height="561"><polygon points="890,110 1146,561 400,561 311,446" fill="#dcdcdc"/></svg></div>
  <svg class="abs leaf" style="top:1162px" width="32" height="20"><use href="#sprout"/></svg>
  <h2 class="abs section-title" style="top:1188px">MARISOL'S <span>STORY</span></h2>
  <div class="abs video" role="img" aria-label="Video still of hands holding a phone showing a family photo wall"></div>
  <svg class="abs play" width="98" height="98" viewBox="0 0 98 98"><circle cx="49" cy="49" r="46" fill="rgba(0,0,0,.25)" stroke="#fff" stroke-width="4"/><path d="M40 31l27 18-27 18z" fill="#fff"/></svg>
  <a class="abs btn-story btn-demo" href="#">DEMO TREES</a>
  <a class="abs btn-story btn-pages" href="#">GERALD PEMBERLY PAGES</a>
</section>

<section>
  <svg class="abs leaf" style="top:1740px" width="32" height="20"><use href="#sprout"/></svg>
  <h2 class="abs section-title" style="top:1773px">OUR <span>PRICING</span></h2>

  <div class="abs plan p-free">
    <div class="plan-name">FREE FOREVER</div>
    <div class="plan-price">Free</div>
    <ul>
      <li><svg class="tick"><use href="#tick"/></svg>Invite people to your tree</li>
      <li><svg class="tick"><use href="#tick"/></svg>Share on social media</li>
      <li><svg class="tick"><use href="#tick"/></svg>Unlimited video creation</li>
      <li><svg class="tick"><use href="#tick"/></svg>KinTrailo Web Clipper browser extension</li>
      <li><svg class="tick faded"><use href="#tick"/></svg>Turn off ads</li>
      <li><svg class="tick faded"><use href="#tick"/></svg>Trees can be marked private*</li>
      <li><svg class="tick"><use href="#tick"/></svg>2 Family Trees</li>
      <li><svg class="tick"><use href="#tick"/></svg>1 GB Storage</li>
    </ul>
  </div>
  <div class="abs plan p-std">
    <div class="plan-name">STANDARD</div>
    <div class="plan-price">$19.95/yr</div>
    <ul>
      <li><svg class="tick"><use href="#tick"/></svg>Invite people to your tree</li>
      <li><svg class="tick"><use href="#tick"/></svg>Share on social media</li>
      <li><svg class="tick"><use href="#tick"/></svg>Unlimited video creation</li>
      <li><svg class="tick"><use href="#tick"/></svg>KinTrailo Web Clipper browser extension</li>
      <li><svg class="tick"><use href="#tick"/></svg>Turn off ads</li>
      <li><svg class="tick faded"><use href="#tick"/></svg>Trees can be marked private*</li>
      <li><svg class="tick"><use href="#tick"/></svg>4 Family Trees</li>
      <li><svg class="tick"><use href="#tick"/></svg>2 GB Storage</li>
    </ul>
  </div>
  <div class="abs plan p-pro">
    <div class="plan-name">PRO</div>
    <div class="plan-price">$34.95/yr</div>
    <ul>
      <li><svg class="tick"><use href="#tick"/></svg>Invite people to your tree</li>
      <li><svg class="tick"><use href="#tick"/></svg>Share on social media</li>
      <li><svg class="tick"><use href="#tick"/></svg>Unlimited video creation</li>
      <li><svg class="tick"><use href="#tick"/></svg>KinTrailo Web Clipper browser extension</li>
      <li><svg class="tick"><use href="#tick"/></svg>Turn off ads</li>
      <li><svg class="tick"><use href="#tick"/></svg>Trees can be marked private*</li>
      <li><svg class="tick"><use href="#tick"/></svg>10 Family Trees</li>
      <li><svg class="tick"><use href="#tick"/></svg>10 GB Storage</li>
    </ul>
  </div>
  <p class="abs footnote">* No matter which plan you choose, information about living people is always kept private</p>
</section>

<footer>
  <div class="abs footer"></div>
  <div class="abs fcol" style="left:145px"><h3>Company</h3><ul><li><a href="#">About Us</a></li><li><a href="#">Our Video</a></li><li><a href="#">Pricing</a></li></ul></div>
  <div class="abs fcol" style="left:355px"><h3>Resources</h3><ul><li><a href="#">Blog</a></li><li><a href="#">Roadmap</a></li><li><a href="#">Privacy policy</a></li><li><a href="#">Terms of use</a></li></ul></div>
  <div class="abs fcol" style="left:592px"><h3>Follow Us</h3><div class="social"><span></span><span></span><span></span><span></span></div></div>
  <div class="abs fbadge" role="img" aria-label="Round badge"></div>
  <div class="abs frule"></div>
  <p class="abs copyright">© 2017 Company Name  All right reserved  Term of Use</p>
</footer>
</body>
</html>
```